Design of a promotional offer flyer required to promote low-cost websites to 1-man band businesses

I want a flyer designed - either a double-sided A5 flyer or even A4 folded into a third double-sided. The flyer is to showcase a new service - low-cost websites for 1-man-band businesses, business startups and tradesmen in England. Look at the copy, find some pix and let me know! Flyer will be printed and used as an image on my website too. Pix could be related to some of the target groups. We need to stress the simple message that websites start from £5 per week and this is an-all-in-one fee.

Target Market(s)

Tradesmen, business start ups and 1-man band businesses that want a website

Industry/Entity Type

Small Business

Contact Information for Business Card

All contact details and name of business to be confirmed shortly

Font styles to use
Serif

Requirements
Must have
• Basic messages from copy for flyer i.e. websites from £5 per week and what each client gets for that price to be included on the business card! Please read copy for the flyer.
Nice to have
• Nice background image or series of small images relevant to the target audience. Again, see list of targets from copy for flyer.
Should not have
• I don't want exact or similar design to my main business Blue Anchor Marketing. The new flyer and business card should be a different and distinct branding to that of Blue Anchor Marketing. Aimed at a more economical style, whilst looking professional, but relevant to the target audiences.

```html
<!DOCTYPE html>
<html lang="en">
<head>
<meta charset="utf-8">
<title>Low-cost websites flyer</title>
<link rel="stylesheet" href="https://fonts.googleapis.com/css2?family=Open+Sans:wght@400;600;700;800&display=swap">
<style>
  :root {
    --navy-deep: #061a2c;
    --navy: #0d3050;
    --ocean: #1f6ca3;
    --sky: #3d9fd2;
    --mist: #a8d3ec;
    --paper: #ffffff;
    --orange: #f7941d;
    --flame: #f25a12;
    --brand-blue: #0a7cc1;
    --ink: #111111;
    --body-ink: #1a1a1a;
  }
  * { margin: 0; padding: 0; box-sizing: border-box; }
  html, body { width: 846px; height: 1200px; overflow: hidden; }
  body { font-family: "Open Sans", Arial, sans-serif; background: var(--paper); }

  .flyer {
    position: relative;
    width: 846px;
    height: 1200px;
    overflow: hidden;
    background:
      radial-gradient(ellipse 700px 500px at 100% 0%, rgba(4,18,32,0.85), rgba(4,18,32,0) 70%),
      linear-gradient(to bottom,
        var(--navy) 0%,
        #123e64 22%,
        var(--ocean) 42%,
        var(--sky) 52%,
        var(--mist) 64%,
        #e8f3fa 72%,
        var(--paper) 80%);
  }

  .headline {
    position: absolute;
    top: 62px;
    left: 0;
    width: 100%;
    text-align: center;
    font-weight: 800;
    font-size: 80px;
    line-height: 1;
    letter-spacing: 1px;
    color: var(--orange);
  }
  .subhead {
    position: absolute;
    top: 150px;
    left: 0;
    width: 100%;
    text-align: center;
    font-weight: 800;
    font-size: 46px;
    line-height: 1;
    color: var(--paper);
  }

  .showcase {
    position: absolute;
    top: 270px;
    left: 55px;
    width: 750px;
    height: 290px;
    border-radius: 4px;
    background: linear-gradient(to right,
      #e9ecef 0%, #f4f1ea 22%, #101c2e 35%, #1c2c44 65%, #bfe2a8 76%, #e6f2fa 86%, #d84a20 100%);
    opacity: 0.92;
  }

  .audience {
    position: absolute;
    top: 596px;
    left: 0;
    width: 100%;
    text-align: center;
    font-weight: 800;
    font-size: 22px;
    line-height: 32px;
    color: var(--paper);
  }

  .price-only {
    position: absolute;
    top: 690px;
    left: 104px;
    font-weight: 700;
    font-size: 176px;
    line-height: 1;
    letter-spacing: -4px;
    color: var(--brand-blue);
  }
  .price-amount {
    position: absolute;
    top: 690px;
    left: 535px;
    font-weight: 700;
    font-size: 176px;
    line-height: 1;
    letter-spacing: -4px;
    color: var(--flame);
  }
  .price-period {
    position: absolute;
    top: 862px;
    left: 540px;
    font-weight: 700;
    font-size: 52px;
    line-height: 1;
    color: var(--ink);
  }
  .price-note {
    position: absolute;
    top: 922px;
    left: 0;
    width: 100%;
    text-align: center;
    font-weight: 700;
    font-size: 66px;
    line-height: 1;
    color: var(--brand-blue);
  }

  .suitable-for {
    position: absolute;
    top: 1046px;
    left: 0;
    width: 100%;
    text-align: center;
    font-weight: 400;
    font-size: 19.5px;
    line-height: 27px;
    color: var(--body-ink);
  }
</style>
</head>
<body>
  <main class="flyer">
    <h1 class="headline">WANT A WEBSITE ?</h1>
    <p class="subhead">WITHOUT IT COSTING THE EARTH?</p>

    <div class="showcase" role="img" aria-label="Row of sample small-business website designs shown in perspective with reflections"></div>

    <p class="audience">PROFESSIONALLY-DESIGNED WEBSITES FOR TRADESMEN,<br>BUSINESS START-UPS AND 1-MAN BANDS FROM</p>

    <p class="price-only">only</p>
    <p class="price-amount">£5</p>
    <p class="price-period">per week</p>
    <p class="price-note">and NO upfront costs!</p>

    <p class="suitable-for">
      Suitable for plumbers, electricians, roofers, builders, painters and decorators,<br>
      joiners, business start-ups, 1-man bands such as hairdressers, photographers, fit-<br>
      ness instructors, window cleaners, beauticians, gardeners, odd job men, wheelie<br>
      bin cleaners, IFAs or self-employed consultants.
    </p>
  </main>
</body>
</html>
```